Payroll Brochure

Create a brochure with the copy i have provided . A simple easy tp read brochure that shows wat we do we handle payroll taxes insurance 401k etc

```html
<!DOCTYPE html>
<html lang="en">
<head>
<meta charset="utf-8">
<title>Brightline – Payroll Brochure</title>
<link href="https://fonts.googleapis.com/css2?family=Montserrat:wght@400;500;600;700&display=swap" rel="stylesheet">
<style>
  :root{
    --wine:#6b1015;
    --wine-deep:#5a0c10;
    --gold:#d98b2b;
    --gold-soft:#e7a94a;
    --ink:#231f20;
    --grey-panel:#e6e6e6;
    --white:#ffffff;
    --page:#ebebeb;
  }
  *{box-sizing:border-box;margin:0;padding:0}
  html,body{width:1200px;height:2941px;overflow:hidden}
  body{background:var(--page);font-family:"Montserrat",Arial,sans-serif;color:var(--ink);position:relative}
  .spread{position:absolute;left:40px;width:1120px;height:790px;background:var(--white);box-shadow:0 4px 18px rgba(0,0,0,.18);overflow:hidden}
  .spread--outer{top:640px}
  .spread--inner{top:1510px}
  .art{position:absolute;inset:0}

  /* outer spread */
  .wordmark{position:absolute;display:flex;align-items:center;gap:12px;font-weight:600;letter-spacing:1px}
  .wordmark i{display:block;background:currentColor}
  .wordmark--front{left:590px;top:38px;font-size:50px;color:var(--wine)}
  .wordmark--front i{width:34px;height:34px;background:var(--gold)}
  .tagline{position:absolute;left:592px;top:112px;font-size:9px;color:#777}
  .wordmark--back{left:222px;top:278px;font-size:34px;color:var(--white)}
  .wordmark--back i{width:20px;height:20px}

  .headline{position:absolute;left:591px;top:562px;color:var(--white);font-weight:700;font-size:33px;line-height:38px;letter-spacing:0}
  .subline{position:absolute;left:592px;top:652px;width:270px;color:var(--gold);font-size:12px;line-height:16px}
  .service-tabs{position:absolute;left:578px;top:735px;width:520px;display:flex}
  .service-tabs li{list-style:none;flex:1;text-align:center;color:var(--white);font-size:11.5px;line-height:14px;border-left:1px solid var(--gold)}
  .service-tabs li:first-child{border-left:none}

  .contact-ask{position:absolute;left:32px;top:650px;color:var(--white);font-weight:600;font-size:16px;line-height:20px}
  .contact-lines{position:absolute;left:32px;top:702px;color:var(--white);font-size:12px;line-height:17px}
  .contact-lines svg{vertical-align:-2px;margin-right:4px}
  .contact-foot{position:absolute;left:32px;top:742px;display:flex;align-items:center;color:var(--white);font-size:12px}
  .contact-foot .office{font-size:8.5px;line-height:11px;border-left:1px solid var(--gold);border-right:1px solid var(--gold);padding:0 20px;margin:0 20px}
  .social{display:flex;align-items:center;gap:6px;font-size:8.5px}
  .social small{font-size:6.5px;line-height:7px;text-align:center;margin-right:4px}
  .social span.dot{width:10px;height:10px;border-radius:50%;background:var(--white)}

  /* inner spread */
  .why{position:absolute;left:0;top:0;width:257px;height:790px;background:var(--grey-panel)}
  .why__photo{position:absolute;left:0;top:0;width:257px;height:192px;background:linear-gradient(120deg,#8a8580 0%,#c9b69a 45%,#f0b45a 100%)}
  .why h2{position:absolute;left:32px;top:214px;width:200px;font-size:14px;line-height:17px;font-weight:500;color:var(--wine)}
  .why__item{position:absolute;left:32px;width:210px;display:flex;gap:12px}
  .why__icon{flex:0 0 22px;height:22px;margin-top:12px;transform:rotate(45deg);background:var(--wine);border:2px solid var(--white);outline:1px solid var(--wine)}
  .why__item h3{font-size:10px;font-weight:500;color:var(--gold);margin-bottom:2px}
  .why__item p{font-size:8.6px;line-height:12.6px}

  .services-title{position:absolute;left:293px;top:30px;display:flex;align-items:center;gap:12px;color:var(--wine);font-weight:600;font-size:21px}
  .services-title i{width:22px;height:22px;border:2px solid var(--wine);transform:rotate(45deg)}
  .col{position:absolute;width:232px;font-size:8.1px;line-height:11.4px}
  .col h4{font-size:11px;font-weight:500;color:var(--wine);margin:9px 0 5px}
  .col p{margin-bottom:6px}
  .col b{font-weight:600}
  .col ul{list-style:none}
  .col li::before{content:"☑";margin-right:5px;color:#555}
  .col--a{left:293px;top:84px}
  .col--b{left:592px;top:162px}
  .col--c{left:852px;top:162px}

  .thumbs{position:absolute;left:592px;top:35px;display:flex;gap:15px}
  .thumb{width:113px;background:#e6e6e6;text-align:center;color:var(--wine);font-size:10px;line-height:12px;padding-bottom:5px}
  .thumb__img{height:62px;margin-bottom:5px}
</style>
</head>
<body>

<!-- Outer spread: back panel and front cover -->
<section class="spread spread--outer" aria-label="Brochure outside">
  <svg class="art" width="1120" height="790" viewBox="0 0 1120 790">
    <defs>
      <linearGradient id="goldFade" x1="0" y1="0" x2="1" y2="1">
        <stop offset="0" stop-color="#fbe7c4"/><stop offset="1" stop-color="#e09a35"/>
      </linearGradient>
      <linearGradient id="chip" x1="0" y1="0" x2="1" y2="1">
        <stop offset="0" stop-color="#f0b24b"/><stop offset="1" stop-color="#8a2a14"/>
      </linearGradient>
    </defs>
    <polygon points="0,0 358,0 1120,720 1120,790 0,790" fill="var(--wine)"/>
    <polygon points="805,0 1120,0 1120,470" fill="url(#goldFade)" role="img" aria-label="Photo of hands at a desk in warm golden light"/>
    <g role="img" aria-label="Photo of hands using a calculator">
      <rect x="628" y="267" width="100" height="100" transform="rotate(45 678 317)" fill="#d9d2cc"/>
    </g>
    <g role="img" aria-label="Photo of a hand touching an HR interface">
      <rect x="728" y="342" width="100" height="100" transform="rotate(45 778 392)" fill="#3f5c86"/>
    </g>
    <g role="img" aria-label="Photo of a smiling business team">
      <rect x="828" y="432" width="100" height="100" transform="rotate(45 878 482)" fill="#8d8f96"/>
    </g>
    <g role="img" aria-label="Photo of a yellow hard hat on a desk">
      <rect x="965" y="565" width="90" height="90" transform="rotate(45 1010 610)" fill="#d4a53f"/>
    </g>
    <rect x="616" y="178" width="28" height="28" transform="rotate(45 630 192)" fill="var(--wine)"/>
    <rect x="619" y="209" width="28" height="28" transform="rotate(45 633 223)" fill="url(#chip)"/>
    <rect x="1070" y="668" width="24" height="24" transform="rotate(45 1082 680)" fill="var(--wine)"/>
  </svg>

  <div class="wordmark wordmark--back"><i></i>Brightline</div>
  <div class="wordmark wordmark--front"><i></i>Brightline</div>
  <p class="tagline">Payroll &amp; Human Resource Outsourcing Company</p>

  <h1 class="headline">THE BRIGHTLINE<br>ADVANTAGE</h1>
  <p class="subline">We are ready to provide you with the benefit management services you need!</p>
  <ul class="service-tabs">
    <li>Payroll<br>Management</li><li>Human<br>Resources</li><li>Employee<br>Benefits</li><li>Workers’<br>Compensation</li>
  </ul>

  <p class="contact-ask">Would you like more information<br>about Brightline services?</p>
  <p class="contact-lines">
    <svg width="11" height="11" viewBox="0 0 24 24"><path fill="#fff" d="M6.6 10.8a15 15 0 006.6 6.6l2.2-2.2c.3-.3.7-.4 1-.2 1.1.4 2.3.6 3.6.6.6 0 1 .4 1 1V20c0 .6-.4 1-1 1A17 17 0 013 4c0-.6.4-1 1-1h3.5c.6 0 1 .4 1 1 0 1.3.2 2.5.6 3.6.1.3 0 .7-.2 1z"/></svg>(800) 555-0142<br>
    <svg width="11" height="11" viewBox="0 0 24 24"><path fill="#fff" d="M2 5h20v14H2z M2 5l10 8 10-8" stroke="#6b1015" stroke-width="1.5"/></svg>hello@brightlinepay.com
  </p>
  <div class="contact-foot">
    <span>www.brightlinepay.com</span>
    <span class="office">120 Harbor Ave Riverton, NY 12000<br>Our office is open 9am to 5pm (EST)</span>
    <span class="social"><small>CONNECT<br>WITH US</small><span class="dot"></span><span class="dot"></span>@BrightlinePay</span>
  </div>
</section>

<!-- Inner spread -->
<section class="spread spread--inner" aria-label="Brochure inside">
  <aside class="why">
    <div class="why__photo" role="img" aria-label="Photo of a business team meeting around a table"></div>
    <h2>What makes Brightline uniquely qualified to be your service provider?</h2>
    <div class="why__item" style="top:268px"><span class="why__icon"></span><div><h3>People</h3><p>Brightline has gone to great lengths to hire and train a world-class team of experienced payroll and HR professionals that are genuinely interested in making sure our clients receive the very best in service and support.</p></div></div>
    <div class="why__item" style="top:424px"><span class="why__icon"></span><div><h3>Process</h3><p>Developed over the years, the Brightline process has been designed with speed and accuracy in mind. Brightline does what’s needed to make sure our clients are presented with speedy responses to their questions, and produce accurate, reliable, and timely payrolls. With Brightline’s custom designed software, we can easily tailor to your payroll needs.</p></div></div>
    <div class="why__item" style="top:610px"><span class="why__icon"></span><div><h3>Products</h3><p>Brightline has developed a comprehensive suite of products and services that will fit your needs.</p></div></div>
    <div class="why__item" style="top:690px"><span class="why__icon"></span><div><h3>Flexibility</h3><p>Brightline will design HR solutions that meet your specific needs and requirements.</p></div></div>
  </aside>

  <h2 class="services-title"><i></i>OUR SERVICES</h2>

  <div class="col col--a">
    <h4>Payroll</h4>
    <p><b>Flexible:</b> Brightline’s flexible and powerful payroll module allows you the ability to grow you’re your business by meeting your unique needs. Supporting payrolls for very large to very small companies.</p>
    <p><b>Efficient:</b> Get payroll done efficiently and accurately by relying on our flexible design to handle even the most complex payroll needs.</p>
    <p><b>Grow without Growing Pains:</b> Brightline’s technology and design is able to allow you to scale your business without adding all the incremental costs typically required.</p>
    <h4>Tax Reporting &amp; Payments</h4>
    <p><b>Accurate:</b> All payroll taxes (federal, state, local) are calculated accurately. Additionally, we determine proper local tax jurisdictions based on the employee home and work addresses.</p>
    <p><b>Complete:</b> Federal, State and Local withholding taxes as well as State and Federal Unemployment taxes are provided. Tax payments are integrated into the Accounts Payable and General Ledger modules.</p>
    <h4>Human Resources</h4>
    <p>With our online HR tools, you can empower yourself to take control of your human resource needs or let us do it.</p>
    <p><b>Get Big Company Services:</b> By using our online tools in conjunction with your service team, you will have access to HR services only afforded by some of the largest companies.</p>
    <p><b>Library:</b> Our online document library lets you and employees create your own library of information accessible at any time. Employees can upload documents and forms that can be kept in history as long as needed.</p>
    <h4>Benefit Enrollment</h4>
    <p><b>Easy and Quick Enrollment:</b> Our intuitive user experience quickly walks employees through their benefit enrollment process and allows them to compare different plans and select those that best meet their life needs.</p>
    <p><b>Flexible Benefit Plans and Easy Setup Options:</b> Offer your clients Fortune 500 benefit plans or administer their plans in an easy to use, yet flexible benefit administration module.</p>
  </div>

  <div class="thumbs">
    <div class="thumb"><div class="thumb__img" role="img" aria-label="Photo of hands using a calculator" style="background:#d9d2cc"></div>Payroll<br>Management</div>
    <div class="thumb"><div class="thumb__img" role="img" aria-label="Photo of an HR touch interface" style="background:#3f5c86"></div>Human<br>Resources</div>
    <div class="thumb"><div class="thumb__img" role="img" aria-label="Photo of a business team" style="background:#8d8f96"></div>Employee<br>Benefits</div>
    <div class="thumb"><div class="thumb__img" role="img" aria-label="Photo of a hard hat on a desk" style="background:#d4a53f"></div>Workers’<br>Compensation</div>
  </div>

  <div class="col col--b">
    <p><b>You Pick:</b> Our flexible contribution setup features, you can contribute in any manner to your employees’ benefits while the system automatically processes them through payroll.</p>
    <h4>On Boarding</h4>
    <p><b>Customize your On Boarding:</b> You can customize your on boarding experience to your hiring needs as well as provide multiple workflows for different employee types. The on boarding experience can be branded for you, providing a personalized experience for the employees.</p>
    <p><b>Custom Document Management:</b> Our custom document mapping feature lets you use your own forms and documents as part of the on boarding and hiring process. When these forms are completed – and electronically signed – they stay in history as long as needed.</p>
    <p><b>Intuitive:</b> With a focus on the user experience, your employees will find it easy and quick to get on boarded with you.</p>
    <h4>Applicant Tracking</h4>
    <p><b>Create and Post Jobs:</b> You can create jobs with just a few clicks and post them on all the popular job sites.</p>
    <p><b>Hire the Right People:</b> By posting on popular job boards, as well as a proprietary database of job seekers, you will reach more candidates. You can choose to receive profiles of candidates that only match your background and specifications.</p>
    <p><b>Manage the Hiring Process:</b> Review candidates via video or online conferencing, review voice interviews, schedule in person interviews, have candidates answer certain online questions and manage this entire process to find the right people. Once hired, they can be on boarded automatically.</p>
    <h4>Time and Attendance</h4>
    <p><b>Make Time Entry Easy:</b> Simplify time tracking so you can spend less time on payroll tasks.</p>
    <p><b>Everywhere Access:</b> Web interface, mobile apps and on-premise time clocks allow employees to log their time wherever they are.</p>
    <p><b>Plug and Play Time Clocks:</b> Time clocks are delivered ready-to-use with little or no setup required.</p>
  </div>

  <div class="col col--c">
    <h4 style="margin-top:0">ACA Compliance</h4>
    <p><b>Client Tools:</b> Provide you with reporting and analysis tools online so you can monitor ACA information and be proactive in managing your needs.</p>
    <p><b>Affordability Test:</b> Provide your with information about plan affordability with their employees so they can stay in compliance.</p>
    <p><b>Large Employer Analysis:</b> Analyze your control groups to determine if you will fall under the rules of ACA for large employer groups.</p>
    <h4>Self Service</h4>
    <p><b>Manager:</b> Your managers have access to their information via a highly intuitive online portal. Users can enter payroll time, create ad-hoc reports, preview and approve payroll and invoices, get invoice and check history, access employee records, communicate with employees, create, etc. Our single sign on allows managers that may have multiple business entities with one login.</p>
    <p><b>Employee:</b> Employees can access pay information, request PTO, enroll in benefits, communicate with other employees, and access/change their personal information. They can also access corporate documents for review and upload personal documents as well.</p>
    <h4>Work Opportunity Tax Credits</h4>
    <p><b>Big Credits:</b> Work Opportunity Tax Credits (WOTC) allow you to receive between $2,400 and $9,600 for hiring eligible employees.</p>
    <p><b>Easy and Quick:</b> Employees complete a simple questionnaire to determine eligibility for WOTC. All of the necessary filing and reporting is handled for you and your client.</p>
    <p><b>Integrated:</b> WOTC is integrated wherever you would enter a new employee – back office payroll, online on boarding, and applicant tracking to ensure all employees are being evaluated.</p>
    <h4>Workers Compensation &amp; Benefits</h4>
    <p><b>Pay as you go Workers’ Compensation:</b> Multiple carriers available.</p>
    <ul><li>Access to a Multiple Employer 401K.</li><li>Access to various voluntary benefits.</li></ul>
  </div>
</section>

</body>
</html>
```